VORTIQ Business Card Design

We need a business card for a new company based on the Gold Coast, we are a new supplement distributing company called VORTIQ Sports Nutrition - Bold Horizon Sports Nutrition. We are providing new science based bodybuilding and fitness supplementation. Our company has a key focus towards next generation. We are wanting a card that is cool, innovative and fresh. We would like to see the implementation of the below image in a fresh and very innovative design that stands out. The final design should communicate New, Innovative, Cool, Science and researched based.
Target Market(s)
The target market is fitness and bodybuilder enthusiasts. Young audience so very cool looking.
Industry/Entity Type
Fitness
Contact Information for Business Card
(front of card)
VORTIQ Sports Nutrition.
Milo Harrow
CEO/Sport Nutrition Specialist
0473 628 904
Milo@vortiqfuelworks.example
www.vortiqfuelworks.example
(back of card)
Scientifically formulated supplement range
Private Nutrition consultations
comprehensive sports nutrition seminars
Requirements
Nice to have
- The card could have a cut out on one of the sides or one of the corners rounded off so the card looks different from a normal business card.
Should not have
- The colours need to complement each other and pop out.

```html
<!DOCTYPE html>
<html lang="en">
<head>
<meta charset="utf-8">
<title>VORTIQ Sports Nutrition – Business Card</title>
<link rel="stylesheet" href="https://fonts.googleapis.com/css2?family=Cinzel:wght@600;700&display=swap">
<style>
  :root {
    --bg: #3a2f3c;
    --card-top: #12414c;
    --card-mid: #0a2229;
    --card-deep: #020607;
    --accent: #5cc6e4;
    --ink: #f2f6f7;
    --ink-soft: #cfd9dc;
  }
  * { box-sizing: border-box; margin: 0; padding: 0; }
  html, body { width: 1200px; height: 900px; overflow: hidden; }
  body {
    background: var(--bg);
    font-family: "Cinzel", "Times New Roman", serif;
    color: var(--ink);
    position: relative;
  }
  .card {
    position: absolute;
    width: 540px;
    height: 310px;
    border-radius: 4px;
    background: radial-gradient(ellipse 90% 110% at 18% 8%, var(--card-top) 0%, var(--card-mid) 45%, var(--card-deep) 100%);
    box-shadow: 0 18px 40px rgba(0,0,0,.45);
    overflow: hidden;
  }
  .card--back { left: 70px; top: 500px; }
  .card--front { left: 590px; top: 130px; }

  /* brand block */
  .brand { display: flex; flex-direction: column; align-items: center; }
  .brand__name {
    display: flex; align-items: center; gap: 10px;
    font-weight: 700; color: var(--accent);
    letter-spacing: 4px;
  }
  .brand__dot { width: 16px; height: 16px; border-radius: 50%; background: var(--accent); }
  .brand__tagline {
    font-weight: 600; font-size: 9.5px; letter-spacing: .6px;
    color: var(--ink); margin-top: 6px; text-transform: uppercase;
  }

  /* back */
  .services {
    position: absolute; left: 0; right: 0; top: 34px;
    list-style: none; text-align: center;
    font-weight: 700; font-size: 17px; line-height: 1.3;
  }
  .card--back .brand { position: absolute; left: 0; right: 0; top: 176px; }
  .card--back .brand__name { font-size: 40px; }

  /* front */
  .card--front .brand { position: absolute; left: 28px; top: 110px; width: 220px; }
  .card--front .brand__name { font-size: 38px; }
  .divider {
    position: absolute; left: 268px; top: 62px; width: 2px; height: 190px;
    background: var(--accent);
  }
  .contact { position: absolute; left: 290px; top: 70px; }
  .contact__name { font-weight: 700; font-size: 24px; color: var(--accent); letter-spacing: .5px; }
  .contact__role { font-weight: 600; font-size: 12px; color: var(--ink-soft); margin-top: 2px; }
  .contact__list { list-style: none; margin-top: 18px; }
  .contact__item {
    display: flex; align-items: center; gap: 10px;
    font-weight: 700; font-size: 12.5px; height: 30px;
  }
  .contact__item--phone { font-size: 16px; letter-spacing: 1px; }
  .contact__item--small { font-size: 10.5px; }
  .icon {
    width: 20px; height: 20px; border: 1.5px solid var(--ink-soft); border-radius: 50%;
    display: flex; align-items: center; justify-content: center; flex: none;
  }
  .icon svg { width: 11px; height: 11px; stroke: var(--ink); fill: none; stroke-width: 1.6; }
</style>
</head>
<body>

  <section class="card card--back" aria-label="Business card back">
    <ul class="services">
      <li>Scientifically Formulated Supplement Range</li>
      <li>Private Nutrition Consultations</li>
      <li>Comprehensive Sports Nutrition</li>
      <li>Seminars</li>
    </ul>
    <div class="brand">
      <div class="brand__name"><span class="brand__dot"></span>VORTIQ</div>
      <div class="brand__tagline">Bold Horizon Sports Nutrition.</div>
    </div>
  </section>

  <section class="card card--front" aria-label="Business card front">
    <div class="brand">
      <div class="brand__name"><span class="brand__dot"></span>VORTIQ</div>
      <div class="brand__tagline">Bold Horizon Sports Nutrition</div>
    </div>
    <div class="divider"></div>
    <div class="contact">
      <div class="contact__name">Milo Harrow</div>
      <div class="contact__role">CEO/Sport Nutrition Specialist</div>
      <ul class="contact__list">
        <li class="contact__item contact__item--phone">
          <span class="icon"><svg viewBox="0 0 12 12"><path d="M3 1.5 L4.6 3.6 L3.6 4.8 Q4.6 7 7.2 8.4 L8.4 7.4 L10.5 9 L9.4 10.6 Q4.8 10.2 1.6 3 Z"/></svg></span>
          0473 628 904
        </li>
        <li class="contact__item contact__item--small">
          <span class="icon"><svg viewBox="0 0 12 12"><rect x="1.5" y="3" width="9" height="6"/><path d="M1.5 3 L6 6.5 L10.5 3"/></svg></span>
          Milo@vortiqfuelworks.example
        </li>
        <li class="contact__item contact__item--small">
          <span class="icon"><svg viewBox="0 0 12 12"><circle cx="6" cy="6" r="4.5"/><ellipse cx="6" cy="6" rx="2" ry="4.5"/><path d="M1.5 6 H10.5"/></svg></span>
          www.vortiqfuelworks.example
        </li>
      </ul>
    </div>
  </section>

</body>
</html>
```